Upscale business cards needed for Board of Directors

We need professional business cards created for members of our family business Board of Directors. We would like these relatively simple and straightforward, but also with a unique element to set them apart. Probably stick with neutral and simple colors - white, grey etc. We need space for the traditional elements, including name, title, address, email/phone number. And we will be creating several from this template so it needs to be template that is easy to switch information in and out of.
Business
See description

```html
<!DOCTYPE html>
<html lang="en">
<head>
<meta charset="UTF-8">
<title>Harborline Holdings – Business Cards</title>
<link rel="stylesheet" href="https://fonts.googleapis.com/css2?family=Roboto:wght@400;700&display=swap">
<style>
  :root {
    --bg-center: #8a8a8a;
    --bg-edge: #1c1c1c;
    --card-black: #231f20;
    --card-white: #ffffff;
    --gold: #b8a67a;
    --text-dark: #231f20;
    --text-light: #ffffff;
    --text-muted: #d8d8d8;
  }
  * { margin: 0; padding: 0; box-sizing: border-box; }
  html, body { width: 1200px; height: 950px; overflow: hidden; }
  body {
    background: radial-gradient(ellipse at 50% 40%, var(--bg-center) 0%, #4a4a4a 45%, var(--bg-edge) 100%);
    font-family: "Roboto", Arial, sans-serif;
    position: relative;
  }
  .card {
    position: absolute;
    left: 250px;
    width: 700px;
    height: 400px;
    overflow: hidden;
    box-shadow: 0 18px 40px rgba(0,0,0,0.55);
  }
  .card-back { top: 55px; background: var(--card-black); }
  .card-front { top: 495px; background: var(--card-white); }

  .wordmark {
    font-family: "Roboto", Arial, sans-serif;
    font-weight: 700;
    text-transform: uppercase;
    letter-spacing: 0.06em;
    white-space: nowrap;
  }
  .card-back .wordmark {
    position: absolute; left: 0; right: 0; top: 160px;
    text-align: center; font-size: 40px; color: var(--text-light);
  }
  .card-back .website {
    position: absolute; left: 0; right: 0; top: 262px;
    text-align: center; font-size: 13px; letter-spacing: 0.35em;
    color: var(--text-muted);
  }

  .front-shapes { position: absolute; inset: 0; }
  .card-front .wordmark {
    position: absolute; right: 52px; top: 112px;
    font-size: 30px; color: var(--text-dark);
  }
  .holder {
    position: absolute; left: 36px; top: 246px; color: var(--text-light);
  }
  .holder-name { font-size: 20px; font-weight: 700; line-height: 1.2; }
  .holder-title { font-size: 14px; line-height: 1.4; }

  .contacts {
    position: absolute; left: 36px; top: 320px; list-style: none;
    color: var(--text-light); font-size: 14px;
  }
  .contacts li { display: flex; align-items: center; gap: 12px; height: 22px; }
  .contacts svg { width: 14px; height: 14px; flex: none; }

  .address {
    position: absolute; right: 36px; top: 246px; text-align: right;
    color: var(--text-light); font-size: 14px; line-height: 1.45;
  }
</style>
</head>
<body>

  <section class="card card-back" aria-label="Card back">
    <div class="wordmark">Harborline Holdings</div>
    <div class="website">www.harborline.com</div>
  </section>

  <section class="card card-front" aria-label="Card front">
    <svg class="front-shapes" viewBox="0 0 700 400" width="700" height="400" aria-hidden="true">
      <polygon fill="var(--gold)" points="0,236 250,236 285,206 700,206 700,400 0,400"/>
      <polygon fill="var(--card-black)" points="0,306 300,306 340,220 700,220 700,400 0,400"/>
    </svg>

    <div class="wordmark">Harborline Holdings</div>

    <div class="holder">
      <div class="holder-name">Mark Ellison</div>
      <div class="holder-title">President</div>
    </div>

    <ul class="contacts">
      <li>
        <svg viewBox="0 0 16 16" aria-hidden="true"><path fill="#fff" d="M3.5 1.5l2.5 0 1 3.5-1.6 1.2a9 9 0 0 0 4.4 4.4L11 9l3.5 1v2.5c0 1-.8 1.8-1.8 1.8A12.5 12.5 0 0 1 1.7 3.3c0-1 .8-1.8 1.8-1.8z"/></svg>
        <span>555 0142 7788</span>
      </li>
      <li>
        <svg viewBox="0 0 16 16" aria-hidden="true"><rect x="1" y="3" width="14" height="10" rx="1" fill="#fff"/><path d="M1.5 3.8L8 9l6.5-5.2" fill="none" stroke="var(--card-black)" stroke-width="1.4"/></svg>
        <span>mark@harborline.com</span>
      </li>
      <li>
        <svg viewBox="0 0 16 16" aria-hidden="true"><circle cx="8" cy="8" r="6.5" fill="none" stroke="#fff" stroke-width="1.5"/><ellipse cx="8" cy="8" rx="2.8" ry="6.5" fill="none" stroke="#fff" stroke-width="1.2"/><path d="M1.5 8h13" stroke="#fff" stroke-width="1.2"/></svg>
        <span>www.harborline.com</span>
      </li>
    </ul>

    <address class="address" style="font-style:normal">
      1270 Alder Crest Lane<br>
      Maple Grove, NY 10920
    </address>
  </section>

</body>
</html>
```